Business Card Design Project

I am looking for a simple business card. I have a logo which I love and have attached. I just need the card to include the logo and the following:
Wanda Pellering
Health & Lifestyle Coach
614/352-8097
wanda@nurtureandmendnation.example
www.pledgetomend.example
Updates
Thank you all for your time and designs, they are great! I chose the business card design that I fell in love with at first sight! Thanks again!
Target Market(s)
businesses looking for corporate wellness.
Industry/Entity Type
Business
Look and feel
Each slider illustrates characteristics of the customer's brand and the style your logo design should communicate.

```html
<!DOCTYPE html>
<html lang="en">
<head>
<meta charset="utf-8">
<title>Wanda Pellering – Business Card</title>
<link rel="stylesheet" href="https://fonts.googleapis.com/css2?family=Work+Sans:wght@400&display=swap">
<style>
  :root {
    --card-white: #ffffff;
    --panel-green: #2f9a48;
    --brand-green: #7cbf3a;
    --ink-dark: #22251c;
    --ink-light: #e9efe7;
  }
  html, body {
    margin: 0;
    padding: 0;
    width: 1200px;
    height: 564px;
    overflow: hidden;
    background: var(--card-white);
  }
  .card {
    position: relative;
    width: 1200px;
    height: 564px;
    display: flex;
    font-family: "Work Sans", Arial, sans-serif;
  }
  .brand-side {
    position: relative;
    width: 603px;
    height: 100%;
    background: var(--card-white);
  }
  .brand-dot {
    position: absolute;
    left: 152px;
    top: 146px;
    width: 150px;
    height: 150px;
    border-radius: 50%;
    background: var(--brand-green);
  }
  .brand-name {
    position: absolute;
    left: 62px;
    top: 318px;
    margin: 0;
    font-size: 64px;
    line-height: 76px;
    font-weight: 400;
    color: var(--ink-dark);
    white-space: nowrap;
  }
  .contact-side {
    width: 597px;
    height: 100%;
    background: var(--panel-green);
    text-align: center;
    box-sizing: border-box;
    padding-top: 148px;
  }
  .person-name {
    margin: 0;
    font-size: 52px;
    font-weight: 400;
    line-height: 58px;
    color: var(--ink-dark);
    white-space: nowrap;
  }
  .person-role {
    margin: 0;
    font-size: 42px;
    font-weight: 400;
    line-height: 46px;
    color: var(--ink-light);
    white-space: nowrap;
  }
  .contact-list {
    list-style: none;
    margin: 44px 0 0;
    padding: 0;
    font-size: 28.5px;
    line-height: 33px;
    color: var(--ink-light);
    white-space: nowrap;
  }
</style>
</head>
<body>
  <main class="card">
    <section class="brand-side">
      <span class="brand-dot"></span>
      <p class="brand-name">Pledge to Mend</p>
    </section>
    <section class="contact-side">
      <h1 class="person-name">Wanda Pellering</h1>
      <p class="person-role">Health &amp; Lifestyle coach</p>
      <ul class="contact-list">
        <li class="contact-phone">614/352-8097</li>
        <li class="contact-email">wanda@nurtureandmendnation.example</li>
        <li class="contact-web">www.pledgetomend.example</li>
      </ul>
    </section>
  </main>
</body>
</html>
```